Brochure design for healthcare software company

We need a tri-fold brochure design for our healthcare software company that provides software and services for clinicians who manage patients who have or may be diagnosed with cancer.

We have an existing web, business card design and trade show booth design and want the ultimate design to be consistent with these. All of the files including stock images are provided.

Target Market(s)

Nurses, Healthcare professionals

Industry/Entity Type

Healthcare

Requirements
Must have
• Design consistent with attached tradeshow booth and business card.

```html
<!DOCTYPE html>
<html lang="en">
<head>
<meta charset="utf-8">
<title>Evenpath – Tri-fold Brochure</title>
<link rel="stylesheet" href="https://fonts.googleapis.com/css2?family=Questrial&display=swap">
<style>
  :root {
    --bg: #eeefee;
    --paper: #ffffff;
    --brand-blue: #1d5aa8;
    --brand-green: #2fb15b;
    --text: #555a60;
    --heading: #3d4247;
    --fold: #e3e4e6;
    --photo-warm-a: #b9c9c6;
    --photo-warm-b: #e9e2d8;
    --photo-blue-a: #5d6fa8;
    --photo-blue-b: #b6c0dc;
    --photo-hands-a: #c9a48e;
    --photo-hands-b: #7e8fb0;
  }
  * { box-sizing: border-box; margin: 0; padding: 0; }
  html, body { width: 1200px; height: 1200px; overflow: hidden; }
  body {
    background: var(--bg);
    font-family: "Questrial", sans-serif;
    color: var(--text);
    position: relative;
  }
  .spread {
    position: absolute;
    width: 720px;
    height: 520px;
    background: var(--paper);
    box-shadow: 0 6px 22px rgba(0,0,0,.12);
  }
  .spread--outside { left: 40px; top: 50px; }
  .spread--inside { left: 440px; top: 630px; }
  .spread svg.art { position: absolute; inset: 0; }
  .panel {
    position: absolute;
    top: 0;
    width: 240px;
    height: 520px;
  }
  .panel--1 { left: 0; }
  .panel--2 { left: 240px; }
  .panel--3 { left: 480px; }

  .wordmark {
    color: var(--brand-blue);
    letter-spacing: .32em;
    text-transform: uppercase;
    font-weight: 400;
    white-space: nowrap;
  }

  /* Outside: feature list */
  .feature-list { list-style: none; position: absolute; left: 26px; top: 70px; }
  .feature-list li {
    display: flex; align-items: center; gap: 12px;
    height: 46px;
    color: var(--brand-blue);
    font-size: 11px;
  }
  .feature-list svg { width: 20px; height: 20px; flex: none; }

  /* Outside: back panel */
  .back-contact {
    position: absolute; left: 0; right: 0; top: 418px;
    text-align: center;
  }
  .back-contact .wordmark { font-size: 8px; display: block; margin-bottom: 12px; }
  .back-contact p { font-size: 7px; line-height: 1.4; color: var(--text); }

  /* Outside: cover */
  .cover-mark {
    position: absolute; left: 0; right: 0; top: 370px;
    text-align: center;
  }
  .cover-mark .wordmark { font-size: 15px; }

  /* Inside copy */
  .copy { position: absolute; left: 22px; right: 20px; }
  .copy h2 { font-size: 12px; color: var(--brand-blue); font-weight: 400; margin-bottom: 14px; }
  .copy h3 { font-size: 10px; color: var(--heading); font-weight: 400; margin-bottom: 5px; }
  .copy p { font-size: 7.4px; line-height: 1.45; margin-bottom: 14px; }
  .panel--1 .copy { top: 34px; }
  .panel--2 .copy { top: 52px; }
  .photo-copy { position: absolute; left: 20px; right: 16px; top: 170px; color: #fff; }
  .photo-copy h3 { font-size: 10px; font-weight: 400; margin-bottom: 4px; color: #fff; }
  .photo-copy p { font-size: 7.4px; line-height: 1.45; }

  /* Lockup */
  .lockup {
    position: absolute; left: 800px; top: 200px; width: 360px;
    text-align: center;
  }
  .lockup .wordmark { font-size: 24px; }
</style>
</head>
<body>

<section class="spread spread--outside">
  <svg class="art" viewBox="0 0 720 520" width="720" height="520">
    <defs>
      <linearGradient id="photoWarm" x1="0" y1="0" x2="1" y2="1">
        <stop offset="0" stop-color="var(--photo-warm-a)"/>
        <stop offset="1" stop-color="var(--photo-warm-b)"/>
      </linearGradient>
    </defs>
    <g role="img" aria-label="Photo of a smiling clinician writing notes at a desk in a bright clinic">
      <path d="M480 0 H720 V222 C640 228 550 250 480 296 Z" fill="url(#photoWarm)"/>
    </g>
    <path class="swoosh" d="M480 296 C550 250 640 228 720 222 V236 C640 246 560 272 480 334 Z" fill="var(--brand-green)"/>
    <path class="swoosh" d="M240 440 C290 360 380 318 480 306 V320 C390 330 300 372 240 472 Z" fill="var(--brand-green)"/>
    <path class="swoosh" d="M0 500 C70 460 160 426 240 412 V426 C160 442 80 480 0 520 Z" fill="var(--brand-green)"/>
    <line x1="240" y1="0" x2="240" y2="520" stroke="var(--fold)"/>
    <line x1="480" y1="0" x2="480" y2="520" stroke="var(--fold)"/>
  </svg>

  <div class="panel panel--1">
    <ul class="feature-list">
      <li><svg viewBox="0 0 20 20"><path d="M10 2 L17 18 L10 14 L3 18 Z" fill="var(--brand-blue)"/></svg>Simplified navigation</li>
      <li><svg viewBox="0 0 20 20"><circle cx="8" cy="8" r="4" fill="none" stroke="var(--brand-blue)" stroke-width="2.5" stroke-dasharray="2 1.5"/><circle cx="14" cy="14" r="3" fill="none" stroke="var(--brand-blue)" stroke-width="2" stroke-dasharray="1.6 1.2"/></svg>Advanced workflow tools</li>
      <li><svg viewBox="0 0 20 20"><circle cx="10" cy="10" r="8" fill="var(--brand-blue)"/><path d="M10 10 V2 M10 10 L17 13 M10 10 L4 15" stroke="#fff" stroke-width="1"/></svg>Reporting and analytics</li>
      <li><svg viewBox="0 0 20 20"><rect x="2" y="2" width="16" height="16" fill="var(--brand-blue)"/><path d="M6 6 L14 14 M14 6 L6 14" stroke="#fff" stroke-width="2.2"/></svg>Eliminate paper</li>
      <li><svg viewBox="0 0 20 20"><circle cx="10" cy="4" r="2.5" fill="var(--brand-blue)"/><path d="M10 7 V13 M4 9 H16 M10 13 L6 19 M10 13 L14 19" stroke="var(--brand-blue)" stroke-width="2.4"/></svg>Integrated</li>
      <li><svg viewBox="0 0 20 20"><rect x="4" y="9" width="12" height="9" fill="var(--brand-blue)"/><path d="M7 9 V6 a3 3 0 0 1 6 0 V9" fill="none" stroke="var(--brand-blue)" stroke-width="2"/></svg>Secure</li>
      <li><svg viewBox="0 0 20 20"><path d="M3 11 L8 16 L17 3" fill="none" stroke="var(--brand-blue)" stroke-width="2.4"/></svg>Affordable</li>
    </ul>
  </div>

  <div class="panel panel--2">
    <div class="back-contact">
      <span class="wordmark">Evenpath</span>
      <p>(800) 555-0172</p>
      <p>www.evenpathhealth.com</p>
      <p>support@evenpathhealth.com</p>
      <p>info@evenpathhealth.com</p>
    </div>
  </div>

  <div class="panel panel--3">
    <div class="cover-mark"><span class="wordmark">Evenpath</span></div>
  </div>
</section>

<div class="lockup"><span class="wordmark">Evenpath</span></div>

<section class="spread spread--inside">
  <svg class="art" viewBox="0 0 720 520" width="720" height="520">
    <defs>
      <linearGradient id="photoBlue" x1="0" y1="0" x2="1" y2="1">
        <stop offset="0" stop-color="var(--photo-blue-b)"/>
        <stop offset="1" stop-color="var(--photo-blue-a)"/>
      </linearGradient>
      <linearGradient id="photoHands" x1="0" y1="0" x2="1" y2="0">
        <stop offset="0" stop-color="var(--photo-hands-b)"/>
        <stop offset=".5" stop-color="var(--photo-hands-a)"/>
        <stop offset="1" stop-color="var(--photo-hands-b)"/>
      </linearGradient>
    </defs>
    <g role="img" aria-label="Photo of a clinician smiling while talking on the phone in a records office, blue toned">
      <path d="M480 0 H720 V280 C640 285 560 300 480 330 Z" fill="url(#photoBlue)"/>
    </g>
    <g role="img" aria-label="Photo of a caregiver holding a patient's hands at a bedside">
      <path d="M0 520 V470 C60 420 140 395 240 395 C320 355 420 345 480 350 C560 320 640 300 720 295 V520 Z" fill="url(#photoHands)"/>
    </g>
    <line x1="240" y1="0" x2="240" y2="520" stroke="var(--fold)"/>
    <line x1="480" y1="0" x2="480" y2="520" stroke="var(--fold)"/>
  </svg>

  <div class="panel panel--1">
    <div class="copy">
      <h2>Evenpath Navigator</h2>
      <h3>Simplified navigation</h3>
      <p>Track all of your patients from their entry point, for example an abnormal imaging result or a positive diagnosis, through treatment. Evenpath Navigator allows you to easily maintain a record of all referrals, exams, treatment notes, appointments and notes for your patients.</p>
      <h3>Advanced workflow tools</h3>
      <p>Streamline steps your entire patient team takes in a single dynamic worklist view. Completely customizable to match your workflow. Create checklists for every step of your workflow to maintain consistent navigation and monitoring.</p>
      <h3>Reporting and analytics</h3>
      <p>Quickly demonstrate the value of your navigation program with easy to use tools and reporting. View patient and provider metrics for any period of your choosing and start tracking data like time to treatment, referrals and appointments.</p>
    </div>
  </div>

  <div class="panel panel--2">
    <div class="copy">
      <h3>Eliminate paper</h3>
      <p>Manage all of your paperwork and patient forms in one easy to use area. Automatically create document packets and auto fill forms for patients or referrals with a single click.</p>
      <h3>Integrated</h3>
      <p>Reduce double data entry by integrating the systems you already have. Patients can be seamlessly added and updated without manual effort.</p>
      <h3>Secure</h3>
      <p>Built from the ground up with security in mind, Evenpath Navigator is completely HIPAA compliant. Rest assured that you and your patients' data is protected.</p>
    </div>
  </div>

  <div class="panel panel--3">
    <div class="photo-copy">
      <h3>Affordable</h3>
      <p>Evenpath Navigator is completely free for an unlimited number of users and facilities. Additional services including deployment, training, consulting and workflow consultations are available.</p>
    </div>
  </div>
</section>

</body>
</html>
```